Redesign cement bags for leading cement producer in south east asia

We are from Larkfield cement and would like to redesign our bag to relaunch the product line. Our bags are made of high quality PP woven sack. We are one of the leading cement producers and we want our bags to have a Larkfield classy look on each visible side when it is loading in a truck or stacking on a pallet.

Thank you for interesting in this project. Good luck.

Project Deadline Extended Reason: Hi all, I have received requests to extend the deadline. Some of the work requires revising and some of them are still on process. To be fair, I also raise my budget to compensate the time. Thanks all for your participation. Added Sunday, July 10, 2016

Target Market(s)

Construction

Industry/Entity Type

Cement

Requirements
Must have
• You will have to design two bags for two cement grades. 52.5 is of higher grade and 42.5 is of lower grade. Both are similar in design but a distinctive colours to differentiate the two at once. Please look at Reference picture 2 for ideas.
Nice to have
• You do not have to change the original logo but the Larkfield cement word font changes are required. There are no restrictions to colours and font but please refrain from using feminine colours. Instructions on rear side of the bags are now included in the scope. Please create new layout and design new user friendly symbols.
Should not have
• Since cement is a dusty product, you need avoid some colours like black as background. The dust need to be less obvious to attract attention. Our previous base colour are shown in below.
• We want a fresh look on our bag, please do not just copy our old design and make small changes. I have attached our competitors' design, please refrain from using their design as well.
• It is recommend to do some research on cement bag sector.

```html
<!DOCTYPE html>
<html lang="en">
<head>
<meta charset="utf-8">
<title>Larkfield Cement – 52.5 Bag Front</title>
<link rel="stylesheet" href="https://fonts.googleapis.com/css2?family=Montserrat:wght@700;800&family=Mulish:wght@500;600;800&display=swap">
<style>
  :root {
    --navy: #1b2d5f;
    --teal: #09a39b;
    --yellow: #ece800;
    --white: #f1f1f1;
    --backdrop: #d9d9d9;
  }
  html, body {
    margin: 0;
    padding: 0;
    width: 1057px;
    height: 1200px;
    overflow: hidden;
    background: var(--backdrop);
  }
  .bag-front {
    position: absolute;
    left: 162px;
    top: 30px;
    width: 733px;
    height: 1140px;
    display: block;
  }
  .fill-yellow { fill: var(--yellow); }
  .fill-teal { fill: var(--teal); }
  .fill-white { fill: var(--white); }
  .fill-navy { fill: var(--navy); }
  .brand-name {
    font-family: "Montserrat", sans-serif;
    font-weight: 800;
    font-size: 104px;
    fill: var(--navy);
  }
  .brand-sub {
    font-family: "Montserrat", sans-serif;
    font-weight: 800;
    font-size: 60px;
    fill: var(--navy);
  }
  .grade-band-label {
    font-family: "Mulish", sans-serif;
    font-weight: 800;
    font-size: 44px;
    fill: var(--white);
  }
  .spec {
    font-family: "Mulish", sans-serif;
    font-weight: 500;
    font-size: 38px;
    fill: var(--navy);
  }
  .spec-strong { font-weight: 800; }
  .origin {
    font-family: "Mulish", sans-serif;
    font-weight: 800;
    font-size: 30px;
    fill: var(--navy);
  }
  .origin-stars {
    font-family: "Mulish", sans-serif;
    font-size: 22px;
    fill: var(--navy);
  }
  .weight-value {
    font-family: "Montserrat", sans-serif;
    font-weight: 700;
    font-size: 66px;
    fill: var(--navy);
  }
  .weight-label {
    font-family: "Mulish", sans-serif;
    font-weight: 600;
    font-size: 36px;
    fill: var(--navy);
  }
</style>
</head>
<body>
  <svg class="bag-front" viewBox="0 0 810 1260" xmlns="http://www.w3.org/2000/svg" aria-label="Larkfield Cement 52.5 bag front panel">
    <!-- background blocks -->
    <rect class="fill-yellow" x="0" y="0" width="810" height="1260"/>
    <polygon class="fill-white" points="0,0 260,0 0,370"/>
    <polygon class="fill-teal" points="250,0 810,0 810,600"/>
    <polygon class="fill-white" points="585,755 745,580 810,645 810,825 740,910"/>
    <polygon class="fill-teal" points="90,1260 405,925 705,1260"/>
    <polygon class="fill-navy" points="585,755 740,910 585,1070 405,910"/>

    <!-- brand -->
    <text class="brand-name" x="405" y="350" text-anchor="middle" textLength="640" lengthAdjust="spacingAndGlyphs">LARKFIELD</text>
    <text class="brand-sub" x="395" y="435" text-anchor="middle" textLength="450" lengthAdjust="spacing">CEMENT</text>

    <!-- product band -->
    <rect class="fill-teal" x="122" y="547" width="566" height="73"/>
    <text class="grade-band-label" x="405" y="600" text-anchor="middle">PORTLAND CEMENT</text>

    <!-- specification -->
    <text class="spec" x="405" y="675" text-anchor="middle">EN 197 – 1 (2000),</text>
    <text class="spec" x="405" y="723" text-anchor="middle">Strength Class <tspan class="spec-strong">52.5</tspan></text>

    <!-- origin -->
    <rect class="fill-navy" x="133" y="910" width="72" height="3"/>
    <rect class="fill-navy" x="288" y="910" width="72" height="3"/>
    <text class="origin-stars" x="246" y="919" text-anchor="middle">★★★</text>
    <text class="origin" x="246" y="955" text-anchor="middle">PRODUCT OF</text>
    <text class="origin" x="246" y="995" text-anchor="middle">MYANMAR</text>

    <!-- quality seal -->
    <circle class="fill-teal" cx="583" cy="935" r="95"/>
    <circle class="fill-navy" cx="583" cy="935" r="60"/>

    <!-- net weight -->
    <text class="weight-value" x="400" y="1138" text-anchor="middle">50 Kg</text>
    <text class="weight-label" x="400" y="1182" text-anchor="middle">Net Weight</text>
  </svg>
</body>
</html>
```